Design a gifting packaging box for clearMOPPS

We have some packaging boxes that we would like to design to send to retailers (buyers) and to influencers. We would like a custom designed box on both sides (inside and outside).

Target Market(s)

Buyers, PR, Influencers

Font styles to use
Other font styles liked:
• Satoshi

Colors
0094D4
00A9DD
6FCCEA
C7EBF8
E9F6FB

Requirements
Must have
• Info on the box to call out

```html
<!DOCTYPE html>
<html lang="en">
<head>
<meta charset="utf-8">
<title>clearMOPPS gifting box dieline</title>
<link rel="stylesheet" href="https://fonts.googleapis.com/css2?family=Poppins:wght@400;500&family=Lato:wght@400&display=swap">
<style>
  :root {
    --bg: #d0e1e5;
    --shadow: #bccfd3;
    --panel: #6ecbea;
    --handle: #68c4da;
    --fold: #3fb4de;
    --cut-line: #c9d3d6;
    --ink: #ffffff;
  }
  html, body { margin: 0; padding: 0; overflow: hidden; background: var(--bg); }
  .canvas { width: 1200px; height: 1200px; position: relative; background: var(--bg); }
  .dieline { position: absolute; inset: 0; width: 1200px; height: 1200px; }
  .shadow { fill: var(--shadow); }
  .panel { fill: var(--panel); }
  .handle { fill: var(--handle); }
  .fold { stroke: var(--fold); stroke-width: 0.8; stroke-dasharray: 2 2; fill: none; }
  .slot { stroke: var(--cut-line); stroke-width: 1.6; }
  .brand { font-family: "Poppins", sans-serif; font-weight: 500; fill: var(--ink); }
  .tagline { font-family: "Poppins", sans-serif; font-weight: 400; fill: var(--ink); }
  .body-copy { font-family: "Lato", sans-serif; font-size: 8.6px; fill: var(--ink); }
  .icon { fill: none; stroke: var(--ink); stroke-width: 1.1; }
</style>
</head>
<body>
<div class="canvas">
<svg class="dieline" viewBox="0 0 1200 1200" xmlns="http://www.w3.org/2000/svg">
  <!-- drop shadows -->
  <g class="shadow" transform="translate(-6 8)">
    <path d="M203 396 H471 V578 H203 A91 91 0 0 1 203 396 Z"/>
    <path d="M739 396 H1007 A91 91 0 0 1 1007 578 H739 Z"/>
    <rect x="387" y="309" width="84" height="84"/>
    <rect x="387" y="582" width="84" height="84"/>
    <path d="M538 215 H672 L692 306 H518 Z"/>
    <path d="M518 669 H692 L672 761 H538 Z"/>
  </g>

  <!-- handles -->
  <path class="handle" fill-rule="evenodd" d="M518 306 L538 222 Q540 215 547 215 H663 Q670 215 672 222 L692 306 Z
    M553 234 H652 Q660 234 662 241 L668 268 Q670 286 660 286 H547 Q538 286 540 268 L546 241 Q548 234 553 234 Z"/>
  <path class="handle" fill-rule="evenodd" d="M518 669 H692 L672 754 Q670 761 663 761 H547 Q540 761 538 754 Z
    M547 690 H660 Q670 690 668 708 L662 735 Q660 742 652 742 H553 Q548 742 546 735 L540 708 Q538 690 547 690 Z"/>

  <!-- tuck flaps -->
  <path class="panel" d="M387 309 H459 L471 306 V396 L459 393 H387 Z"/>
  <path class="panel" d="M823 309 H751 L739 306 V396 L751 393 H823 Z"/>
  <path class="panel" d="M387 582 H459 L471 578 V669 L459 666 H387 Z"/>
  <path class="panel" d="M823 582 H751 L739 578 V669 L751 666 H823 Z"/>

  <!-- main panels -->
  <rect class="panel" x="471" y="306" width="268" height="363"/>
  <path class="panel" d="M203 396 H471 V578 H203 A91 91 0 0 1 203 396 Z"/>
  <path class="panel" d="M739 396 H1007 A91 91 0 0 1 1007 578 H739 Z"/>

  <!-- fold lines -->
  <line class="fold" x1="471" y1="306" x2="471" y2="669"/>
  <line class="fold" x1="739" y1="306" x2="739" y2="669"/>
  <line class="fold" x1="471" y1="396" x2="739" y2="396"/>
  <line class="fold" x1="471" y1="578" x2="739" y2="578"/>
  <line class="fold" x1="380" y1="396" x2="380" y2="578"/>
  <line class="fold" x1="830" y1="396" x2="830" y2="578"/>
  <line class="fold" x1="518" y1="306" x2="692" y2="306"/>
  <line class="fold" x1="518" y1="669" x2="692" y2="669"/>

  <!-- tuck slots -->
  <line class="slot" x1="159" y1="488" x2="333" y2="488"/>
  <line class="slot" x1="877" y1="488" x2="1051" y2="488"/>

  <!-- top panel (upside down) -->
  <g transform="rotate(180 604 350)">
    <text class="brand" x="604" y="361" font-size="17" text-anchor="middle">clearMOPPS</text>
    <text class="tagline" x="655" y="369" font-size="5" text-anchor="end">Clean Care Anywhere</text>
  </g>

  <!-- front panel -->
  <text class="brand" x="604" y="444" font-size="13" text-anchor="middle">clearMOPPS</text>
  <text class="tagline" x="642" y="450" font-size="4" text-anchor="end">Clean Care Anywhere</text>
  <text class="body-copy" x="507" y="489">Lorem ipsum dolor sit amet, consectetuer adipis-</text>
  <text class="body-copy" x="507" y="500.5">cing elit, sed diam nonummy nibh euismod tinci-</text>
  <text class="body-copy" x="507" y="512">dunt ut laoreet dolore magna aliquam erat volut-</text>
  <g class="icon">
    <circle cx="514" cy="555" r="4.2"/>
    <path d="M526 559 Q528 551 535 550 Q534 558 526 559 Z"/>
    <path d="M547 551 Q550 555 550 557 A3 3 0 0 1 544 557 Q544 555 547 551 Z"/>
    <path d="M558 553 L562 551 L566 555 M566 555 L563 559 L559 559 M559 559 L557 555"/>
  </g>

  <!-- left side panel -->
  <g transform="rotate(90 430 488)">
    <text class="brand" x="430" y="492" font-size="17" text-anchor="middle">clearMOPPS</text>
    <text class="tagline" x="481" y="500" font-size="5" text-anchor="end">Clean Care Anywhere</text>
  </g>

  <!-- right side panel -->
  <g transform="rotate(-90 784 488)">
    <text class="brand" x="784" y="486" font-size="17" text-anchor="middle">clearMOPPS</text>
    <text class="tagline" x="835" y="495" font-size="5" text-anchor="end">Clean Care Anywhere</text>
  </g>

  <!-- right lid -->
  <text class="brand" x="963" y="516" font-size="17" text-anchor="middle">clearMOPPS</text>
  <text class="tagline" x="1014" y="525" font-size="5.5" text-anchor="end">Clean Care Anywhere</text>

  <!-- bottom panel -->
  <text class="brand" x="604" y="627" font-size="17" text-anchor="middle">clearMOPPS</text>
  <text class="tagline" x="655" y="636" font-size="5.5" text-anchor="end">Clean Care Anywhere</text>
</svg>
</div>
</body>
</html>
```